1" x 3" label needed for essential oil bottle(s) - new ecommerce company

We need a label designed for 10 ml bottles of essential oils. We are offering 9 different types of essential oil: Lavender, Cedarwood, Eucalyptus, Frankincense, Lemon, Orange, Peppermint, Rosemary, and Tea Tree. The label should have a space for the type of essential oil. The bottles are an amber color (am including a photo) as essential oils are sensitive to light. also am including an AI file of our logo, which we'd like included on the label; the logo file also contains our logo colors, a dark blue and light grey. We'd also like the following on the label: "CAUTION: EYE AND SKIN IRRITANT. Avoid contact with eyes and skin. Wash hands after handling. If eye contact occurs, flush with water for 15 minutes. Not intended for topical or internal use. Contains Essential Oils. KEEP OUT OF REACH OF CHILDREN."
Also "Ingredients: 100% pure essential oil, GC tested."
Also "0.33 fl oz (10 ml)
Finally, we will need to include a sideways bar code on the right side of the label, so need 3/8" of white space on the right of the label.
We'd like the label to be calming, but modern, friendly, and confident.

```html
<!DOCTYPE html>
<html lang="en">
<head>
<meta charset="utf-8">
<title>Calmera Essential Oil Labels</title>
<link href="https://fonts.googleapis.com/css2?family=Lato:wght@400;700&display=swap" rel="stylesheet">
<style>
  :root {
    --backdrop: #c5b3d9;
    --label-paper: #f2efed;
    --label-glow: #ffffff;
    --brand-slate: #4a5660;
    --ink: #505a63;
    --ink-strong: #3d4750;
    --edge: #b8aec4;
    --sprig-tone: #e2dfde;
  }
  * { box-sizing: border-box; margin: 0; padding: 0; }
  html, body { width: 1200px; height: 1200px; overflow: hidden; }
  body {
    background: var(--backdrop);
    font-family: "Lato", sans-serif;
    color: var(--ink);
    position: relative;
  }
  .label {
    position: absolute;
    width: 560px;
    height: 107px;
    background:
      radial-gradient(ellipse 150px 60px at 280px 50px, var(--label-glow) 0%, rgba(255,255,255,0) 100%),
      var(--label-paper);
    border: 1px solid var(--edge);
    overflow: hidden;
    transform-origin: top left;
  }
  .label--hero { transform: scale(1.954, 1.915); border: none; }

  .caution {
    position: absolute;
    left: 20px; top: 11px;
    font-size: 8.6px;
    line-height: 10.4px;
    color: var(--ink);
  }
  .caution strong { font-weight: 700; color: var(--ink-strong); }
  .caution .keep-out { display: block; margin-top: 7px; font-size: 8.8px; }

  .brand {
    position: absolute;
    left: 200px; width: 160px; top: 14px;
    text-align: center;
  }
  .brand-dot {
    width: 18px; height: 18px;
    margin: 0 auto 10px;
    border: 1.3px solid var(--brand-slate);
    border-radius: 50%;
  }
  .brand-name {
    font-size: 17px;
    letter-spacing: 5px;
    padding-left: 5px;
    color: var(--brand-slate);
    font-weight: 400;
    line-height: 1;
  }
  .tagline {
    margin-top: 6px;
    font-size: 5px;
    letter-spacing: 2px;
    padding-left: 2px;
    color: var(--brand-slate);
    white-space: nowrap;
  }
  .purity {
    margin-top: 7px;
    font-size: 7.2px;
    color: #2f363c;
  }

  .sprig {
    position: absolute;
    left: 330px; top: 6px;
    width: 72px; height: 95px;
    border-radius: 36px;
    background: radial-gradient(ellipse at center, var(--sprig-tone) 0%, rgba(226,223,222,0) 75%);
  }

  .oil-band {
    position: absolute;
    left: 409px; top: 0;
    width: 19px; height: 100%;
    background: var(--brand-slate);
  }
  .oil-name, .volume {
    position: absolute;
    top: 0; height: 100%;
    writing-mode: vertical-rl;
    transform: rotate(180deg);
    display: flex; align-items: center; justify-content: center;
    white-space: nowrap;
  }
  .oil-name {
    left: 409px; width: 19px;
    color: #fff;
    font-size: 11px;
    font-weight: 700;
  }
  .volume {
    left: 432px; width: 16px;
    font-size: 8.2px;
    color: #2f363c;
  }
  .barcode-space {
    position: absolute;
    left: 506px; top: 14px;
    width: 40px; height: 80px;
    background: #fff;
  }
</style>
</head>
<body>

<!-- left column -->
<div class="label" style="left:23px; top:24px;">
  <p class="caution"><strong>CAUTION:</strong> EYE AND SKIN IRRITANT.<br>Avoid contact with eyes and skin.<br>Wash hands after handling. If eye contact<br>occurs, flush with waterfor 15 minutes.<br>Not intended for topical or internal use.<br>Contains Essential Oils.<span class="keep-out">KEEP OUT OF REACH OF CHILDREN</span></p>
  <div class="brand"><div class="brand-dot"></div><div class="brand-name">CALMERA</div><div class="tagline">RESTORING CALM TO LIVING</div><div class="purity">100% Pure Essential Oil | GC Tested</div></div>
  <div class="sprig" role="img" aria-label="Line drawing of an orange and orange slice"></div>
  <div class="oil-band"></div><div class="oil-name">ORANGE</div><div class="volume">0.33 fl oz (10 ml)</div>
  <div class="barcode-space"></div>
</div>

<div class="label" style="left:23px; top:143px;">
  <p class="caution"><strong>CAUTION:</strong> EYE AND SKIN IRRITANT.<br>Avoid contact with eyes and skin.<br>Wash hands after handling. If eye contact<br>occurs, flush with waterfor 15 minutes.<br>Not intended for topical or internal use.<br>Contains Essential Oils.<span class="keep-out">KEEP OUT OF REACH OF CHILDREN</span></p>
  <div class="brand"><div class="brand-dot"></div><div class="brand-name">CALMERA</div><div class="tagline">RESTORING CALM TO LIVING</div><div class="purity">100% Pure Essential Oil | GC Tested</div></div>
  <div class="sprig" role="img" aria-label="Line drawing of a peppermint sprig"></div>
  <div class="oil-band"></div><div class="oil-name">PEPPERMINT</div><div class="volume">0.33 fl oz (10 ml)</div>
  <div class="barcode-space"></div>
</div>

<div class="label" style="left:23px; top:263px;">
  <p class="caution"><strong>CAUTION:</strong> EYE AND SKIN IRRITANT.<br>Avoid contact with eyes and skin.<br>Wash hands after handling. If eye contact<br>occurs, flush with waterfor 15 minutes.<br>Not intended for topical or internal use.<br>Contains Essential Oils.<span class="keep-out">KEEP OUT OF REACH OF CHILDREN</span></p>
  <div class="brand"><div class="brand-dot"></div><div class="brand-name">CALMERA</div><div class="tagline">RESTORING CALM TO LIVING</div><div class="purity">100% Pure Essential Oil | GC Tested</div></div>
  <div class="sprig" role="img" aria-label="Line drawing of rosemary sprigs"></div>
  <div class="oil-band"></div><div class="oil-name">ROSEMARY</div><div class="volume">0.33 fl oz (10 ml)</div>
  <div class="barcode-space"></div>
</div>

<div class="label" style="left:23px; top:383px;">
  <p class="caution"><strong>CAUTION:</strong> EYE AND SKIN IRRITANT.<br>Avoid contact with eyes and skin.<br>Wash hands after handling. If eye contact<br>occurs, flush with waterfor 15 minutes.<br>Not intended for topical or internal use.<br>Contains Essential Oils.<span class="keep-out">KEEP OUT OF REACH OF CHILDREN</span></p>
  <div class="brand"><div class="brand-dot"></div><div class="brand-name">CALMERA</div><div class="tagline">RESTORING CALM TO LIVING</div><div class="purity">100% Pure Essential Oil | GC Tested</div></div>
  <div class="sprig" role="img" aria-label="Line drawing of a tea tree branch"></div>
  <div class="oil-band"></div><div class="oil-name">TEA TREE</div><div class="volume">0.33 fl oz (10 ml)</div>
  <div class="barcode-space"></div>
</div>

<!-- right column -->
<div class="label" style="left:617px; top:24px;">
  <p class="caution"><strong>CAUTION:</strong> EYE AND SKIN IRRITANT.<br>Avoid contact with eyes and skin.<br>Wash hands after handling. If eye contact<br>occurs, flush with waterfor 15 minutes.<br>Not intended for topical or internal use.<br>Contains Essential Oils.<span class="keep-out">KEEP OUT OF REACH OF CHILDREN</span></p>
  <div class="brand"><div class="brand-dot"></div><div class="brand-name">CALMERA</div><div class="tagline">RESTORING CALM TO LIVING</div><div class="purity">100% Pure Essential Oil | GC Tested</div></div>
  <div class="sprig" role="img" aria-label="Line drawing of a cedar branch"></div>
  <div class="oil-band"></div><div class="oil-name">CEDARWOOD</div><div class="volume">0.33 fl oz (10 ml)</div>
  <div class="barcode-space"></div>
</div>

<div class="label" style="left:617px; top:143px;">
  <p class="caution"><strong>CAUTION:</strong> EYE AND SKIN IRRITANT.<br>Avoid contact with eyes and skin.<br>Wash hands after handling. If eye contact<br>occurs, flush with waterfor 15 minutes.<br>Not intended for topical or internal use.<br>Contains Essential Oils.<span class="keep-out">KEEP OUT OF REACH OF CHILDREN</span></p>
  <div class="brand"><div class="brand-dot"></div><div class="brand-name">CALMERA</div><div class="tagline">RESTORING CALM TO LIVING</div><div class="purity">100% Pure Essential Oil | GC Tested</div></div>
  <div class="sprig" role="img" aria-label="Line drawing of eucalyptus leaves"></div>
  <div class="oil-band"></div><div class="oil-name">EUCALYPTUS</div><div class="volume">0.33 fl oz (10 ml)</div>
  <div class="barcode-space"></div>
</div>

<div class="label" style="left:617px; top:263px;">
  <p class="caution"><strong>CAUTION:</strong> EYE AND SKIN IRRITANT.<br>Avoid contact with eyes and skin.<br>Wash hands after handling. If eye contact<br>occurs, flush with waterfor 15 minutes.<br>Not intended for topical or internal use.<br>Contains Essential Oils.<span class="keep-out">KEEP OUT OF REACH OF CHILDREN</span></p>
  <div class="brand"><div class="brand-dot"></div><div class="brand-name">CALMERA</div><div class="tagline">RESTORING CALM TO LIVING</div><div class="purity">100% Pure Essential Oil | GC Tested</div></div>
  <div class="sprig" role="img" aria-label="Line drawing of a frankincense branch"></div>
  <div class="oil-band"></div><div class="oil-name">FRANKINCENSE</div><div class="volume">0.33 fl oz (10 ml)</div>
  <div class="barcode-space"></div>
</div>

<div class="label" style="left:617px; top:383px;">
  <p class="caution"><strong>CAUTION:</strong> EYE AND SKIN IRRITANT.<br>Avoid contact with eyes and skin.<br>Wash hands after handling. If eye contact<br>occurs, flush with waterfor 15 minutes.<br>Not intended for topical or internal use.<br>Contains Essential Oils.<span class="keep-out">KEEP OUT OF REACH OF CHILDREN</span></p>
  <div class="brand"><div class="brand-dot"></div><div class="brand-name">CALMERA</div><div class="tagline">RESTORING CALM TO LIVING</div><div class="purity">100% Pure Essential Oil | GC Tested</div></div>
  <div class="sprig" role="img" aria-label="Line drawing of a lemon and lemon slice"></div>
  <div class="oil-band"></div><div class="oil-name">LEMON</div><div class="volume">0.33 fl oz (10 ml)</div>
  <div class="barcode-space"></div>
</div>

<!-- featured label -->
<div class="label label--hero" style="left:60px; top:868px;">
  <p class="caution"><strong>CAUTION:</strong> EYE AND SKIN IRRITANT.<br>Avoid contact with eyes and skin.<br>Wash hands after handling. If eye contact<br>occurs, flush with waterfor 15 minutes.<br>Not intended for topical or internal use.<br>Contains Essential Oils.<span class="keep-out">KEEP OUT OF REACH OF CHILDREN</span></p>
  <div class="brand"><div class="brand-dot"></div><div class="brand-name">CALMERA</div><div class="tagline">RESTORING CALM TO LIVING</div><div class="purity">100% Pure Essential Oil | GC Tested</div></div>
  <div class="sprig" role="img" aria-label="Line drawing of lavender stems"></div>
  <div class="oil-band"></div><div class="oil-name">LAVENDER</div><div class="volume">0.33 fl oz (10 ml)</div>
  <div class="barcode-space"></div>
</div>

</body>
</html>
```